Zielgruppe
Wir sind ein IT Systemhaus mit einem Scherpunkt auf Wireless LAN für Gewerbekunden
https://www.quarvelo-netz.de/wlan-beratung/
Aufgabenstellung
Im Anhang finden Sie einige Stichpunkte/Texte und eine PPT mit Grafiken, sowie unser Briefpapier.
Ziel ist es 1 Flyer A4 Einseitig zu erhalten – Wir benötigen diesen As soon as possible
Das Thema lautet hier:
1. Lernoffensive Klassen
Grafiken können Sie aus der PPT oder der Webseite entnehmen
Die Flyer sollten im oberen Bereich wie unser Briefpapier aussehen und Farbmäßig unserem CD entsprechen
#1e73be
Den Orangeton finde ich leider gerade nicht ☹
An Ergänzenden Grafiken sind wir ebenfalls Interessiert.
Die Welle haben wir leider nicht als Vectorgrafik

```html
<!DOCTYPE html>
<html lang="de">
<head>
<meta charset="utf-8">
<title>Quarvelo Flyer</title>
<link href="https://fonts.googleapis.com/css2?family=Roboto+Condensed:ital,wght@0,400;1,300;1,400;1,600&family=Titillium+Web:ital,wght@0,400;1,600&display=swap" rel="stylesheet">
<style>
:root{
  --bg:#c4c4c4;
  --paper:#ffffff;
  --blue:#1e73be;
  --blue-deep:#1763a8;
  --blue-mid:#3f95d4;
  --blue-light:#a9d4f0;
  --orange:#e8731f;
  --text:#4a4a4a;
  --heading:#3e3e3e;
  --logo:#5a5a5a;
}
*{box-sizing:border-box;margin:0;padding:0}
html,body{width:1200px;height:809px;overflow:hidden;background:var(--bg)}
.canvas{position:relative;width:1200px;height:809px}
.divider{position:absolute;left:587px;top:0;width:14px;height:809px;background:#d8d8d8}
.flyer{position:absolute;top:19px;width:546px;height:773px;background:var(--paper);overflow:hidden;
  font-family:"Roboto Condensed",sans-serif;color:var(--text);box-shadow:0 0 3px rgba(0,0,0,.25)}
.flyer--schools{left:19px}
.flyer--builders{left:627px}
.wave-top,.wave-bottom{position:absolute;left:0;width:546px}
.wave-top{top:0;height:90px}
.wave-bottom{bottom:0;height:80px}
.brand{position:absolute;right:34px;top:40px;font-family:"Titillium Web",sans-serif;font-weight:400;
  font-size:30px;letter-spacing:2px;color:var(--logo)}
.title{position:absolute;left:22px;top:114px;font-family:"Titillium Web",sans-serif;font-style:italic;
  font-weight:600;font-size:28px;line-height:34px;color:var(--blue);white-space:nowrap}
.flyer--builders .title{font-size:30px;top:121px}
.section{position:absolute;left:22px;white-space:nowrap}
.section h3{font-weight:400;font-style:italic;font-size:14.5px;line-height:18px;color:var(--heading);margin-bottom:4px}
.section ul{list-style:none}
.section li{position:relative;padding-left:17px;font-style:italic;font-weight:300;font-size:13px;line-height:18.5px}
.section li::before{content:"•";position:absolute;left:5px;font-style:normal}
.section--wide li{padding-left:21px}
.section li.tight{line-height:15px;padding-top:2px}
.feature{position:absolute;width:120px;text-align:center;font-style:italic;font-weight:600;
  font-size:14.5px;line-height:15px;color:var(--blue)}
.feature svg{display:block;margin:0 auto 5px;width:52px;height:52px}
.photo-main{position:absolute;right:0;bottom:60px}
.photo-round{position:absolute;width:168px;height:168px;border-radius:50%;border:8px solid var(--orange);z-index:2}
.advantages{position:absolute;background:var(--blue);color:#fff;padding:10px 12px 0 19px;z-index:1;white-space:nowrap}
.advantages h3{font-style:italic;font-weight:600;font-size:14.5px;line-height:18px;margin-bottom:7px}
.advantages ul{list-style:none}
.advantages li{position:relative;padding-left:9px;font-style:italic;font-weight:400;font-size:11.5px;line-height:13.2px;margin-bottom:13.2px}
.advantages li::before{content:"•";position:absolute;left:0}
.contact{position:absolute;right:12px;bottom:6px;color:#fff;font-style:italic;font-weight:600;font-size:11.5px;z-index:3}
</style>
</head>
<body>
<div class="canvas">
  <div class="divider"></div>

  <section class="flyer flyer--schools">
    <svg class="wave-top" viewBox="0 0 546 90" preserveAspectRatio="none">
      <path d="M0 0H546V10C420 8 240 20 0 80Z" fill="var(--blue-light)"/>
      <path d="M0 0H470C330 6 190 20 0 58Z" fill="var(--blue-mid)"/>
      <path d="M0 0H430C300 2 160 6 0 28Z" fill="var(--blue)"/>
    </svg>
    <div class="brand">QUARVELO</div>
    <h1 class="title">Lernoffensive Klassen</h1>

    <div class="section" style="top:153px">
      <h3>Mehrwert für die Schule:</h3>
      <ul>
        <li>90% der Kosten werden vom Staat übernommen</li>
        <li>Reputationsvorteil durch digitales Lernangebot</li>
        <li>Moderne Unterrichtsmethoden</li>
      </ul>
    </div>
    <div class="section" style="top:258px">
      <h3>Mehrwert für die Schüler:</h3>
      <ul>
        <li>Routinierter Umgang mit modernen Medien</li>
        <li>Verbesserte Lernerfolge</li>
        <li>Zeitgemäße Medienkompetenzen</li>
      </ul>
    </div>
    <div class="section" style="top:363px">
      <h3>Die Quarvelo GmbH bietet:</h3>
      <ul>
        <li>Unterstützung während der Antragsstellung</li>
        <li>Erfahrung mit Schulen</li>
        <li class="tight">Professionelle WLAN-Beratung<br>von Konzept bis zur Konfiguration</li>
      </ul>
    </div>

    <div class="feature" style="left:361px;top:145px">
      <svg viewBox="0 0 52 52"><rect x="1" y="1" width="50" height="50" rx="9" fill="#fff" stroke="var(--blue)" stroke-width="1.2"/>
        <g fill="none" stroke="var(--orange)" stroke-width="3.5" stroke-linecap="round">
          <path d="M13 22a18 18 0 0 1 26 0"/><path d="M18 27a11 11 0 0 1 16 0"/></g>
        <circle cx="26" cy="34" r="3.5" fill="var(--orange)"/></svg>
      WLAN Lösungen
    </div>
    <div class="feature" style="left:361px;top:240px">
      <svg viewBox="0 0 52 52"><rect x="1" y="1" width="50" height="50" rx="9" fill="#fff" stroke="var(--blue)" stroke-width="1.2"/>
        <rect x="11" y="12" width="30" height="21" rx="2" fill="var(--orange)"/>
        <rect x="23" y="33" width="6" height="5" fill="var(--orange)"/><rect x="18" y="38" width="16" height="2.5" fill="var(--orange)"/>
        <rect x="33" y="31" width="10" height="8" rx="1" fill="var(--blue)"/>
        <path d="M35 31v-3a3 3 0 0 1 6 0v3" fill="none" stroke="var(--blue)" stroke-width="1.6"/></svg>
      IT Sicherheit
    </div>
    <div class="feature" style="left:361px;top:338px">
      <svg viewBox="0 0 52 52"><rect x="1" y="1" width="50" height="50" rx="9" fill="#fff" stroke="var(--blue)" stroke-width="1.2"/>
        <path d="M13 28a13 13 0 0 1 26 0" fill="none" stroke="var(--orange)" stroke-width="3.5"/>
        <rect x="10" y="26" width="6" height="10" rx="2" fill="var(--orange)"/><rect x="36" y="26" width="6" height="10" rx="2" fill="var(--orange)"/>
        <circle cx="37" cy="39" r="6" fill="var(--blue)"/></svg>
      Support vom<br>Fachmann
    </div>

    <div class="photo-main" role="img" aria-label="Foto: Schüler arbeitet lächelnd an einem Tablet im Klassenzimmer"
      style="width:320px;height:250px;background:linear-gradient(135deg,#c9b9a0,#6f8fb5 55%,#2f4f86);clip-path:polygon(0 22%,100% 0,100% 100%,0 100%)"></div>
    <div class="photo-round" role="img" aria-label="Foto: Schülerin arbeitet am Laptop im Unterricht"
      style="left:205px;top:407px;background:linear-gradient(160deg,#e4e6e8,#9fa6ad 60%,#b05a5a)"></div>

    <div class="advantages" style="left:15px;top:484px;width:222px;height:273px">
      <h3>Ihre Vorteile auf einen Blick:</h3>
      <ul>
        <li>Integration von modernen<br>Lernmethoden</li>
        <li>Ständig verfügbare, digitale<br>Lernumgebungen</li>
        <li>Digitale Kommunikationswege<br>zwischen Lehrern und Schülern</li>
        <li>Direktes Feedback für Schüler<br>und Lehrer</li>
        <li>Einbindung von BYOD-Konzepten<br>und Screencasting</li>
        <li>Remote-Zugriff auf den Unterricht<br>von Zuhause</li>
      </ul>
    </div>

    <svg class="wave-bottom" viewBox="0 0 546 80" preserveAspectRatio="none">
      <path d="M240 80V42C350 20 450 8 546 6V80Z" fill="var(--blue-light)"/>
      <path d="M240 80V56C350 38 450 30 546 30V80Z" fill="var(--blue-mid)"/>
      <path d="M0 80V66C180 54 380 48 546 50V80Z" fill="var(--blue-deep)"/>
    </svg>
    <div class="contact">info@quarvelo-netz.de | www.quarvelo-netz.de</div>
  </section>

  <section class="flyer flyer--builders">
    <svg class="wave-top" viewBox="0 0 546 90" preserveAspectRatio="none">
      <path d="M0 0H546V10C420 8 240 20 0 80Z" fill="var(--blue-light)"/>
      <path d="M0 0H470C330 6 190 20 0 58Z" fill="var(--blue-mid)"/>
      <path d="M0 0H430C300 2 160 6 0 28Z" fill="var(--blue)"/>
    </svg>
    <div class="brand">QUARVELO</div>
    <h1 class="title">WLAN für Bauunternehmen &amp; Elektriker</h1>

    <div class="section" style="top:153px">
      <h3>Mehrwerte für Ihr Unternehmen:</h3>
      <ul>
        <li>Alleinstellungsmarkmal gegenüber Mitbewerbern</li>
        <li>Schaffung neuer (monetärer) Mehrwerte</li>
        <li>Risikominderung für WLAN Fehlplanungen</li>
      </ul>
    </div>
    <div class="section" style="top:245px">
      <h3>Mehrwerte für Ihre Kunden:</h3>
      <ul>
        <li>Professionelles WLAN bereits beim Einzug</li>
        <li>WLAN nach Stand der Technik</li>
        <li>Investitionskosten für WLAN bereits im<br>Rahmen der Gebäudefinanzierung planbar</li>
        <li>Investitionskosten über Gebäudefinanzierung<br>planbar</li>
      </ul>
    </div>
    <div class="section section--wide" style="top:389px">
      <h3>Die Quarvelo GmbH bietet:</h3>
      <ul>
        <li>Erfahrung mit Bauvorhaben in privaten<br>und öffentlichen Bereichen</li>
        <li>ISO 9001 und ISO 27001 zertifiziert</li>
        <li>Professionelle WLAN-Beratung<br>von Konzept bis zur<br>Konfiguration</li>
      </ul>
    </div>

    <div class="feature" style="left:361px;top:162px">
      <svg viewBox="0 0 52 52"><rect x="1" y="1" width="50" height="50" rx="9" fill="#fff" stroke="var(--blue)" stroke-width="1.2"/>
        <rect x="11" y="12" width="28" height="26" fill="var(--orange)"/>
        <rect x="16" y="17" width="18" height="15" fill="none" stroke="#fff" stroke-width="1.5"/>
        <path d="M20 32V24h9" fill="none" stroke="#fff" stroke-width="1.5"/>
        <path d="M33 39a7 7 0 0 1 10 0M35.5 41.5a3.5 3.5 0 0 1 5 0" fill="none" stroke="var(--blue)" stroke-width="1.6"/></svg>
      WLAN Planung
    </div>
    <div class="feature" style="left:361px;top:254px">
      <svg viewBox="0 0 52 52"><rect x="1" y="1" width="50" height="50" rx="9" fill="#fff" stroke="var(--blue)" stroke-width="1.2"/>
        <path d="M10 26L26 12L42 26M14 23V40H38V23" fill="none" stroke="var(--orange)" stroke-width="3" stroke-linejoin="round"/>
        <circle cx="26" cy="29" r="2" fill="var(--orange)"/>
        <path d="M21 25a7 7 0 0 1 10 0" fill="none" stroke="var(--orange)" stroke-width="1.6"/>
        <path d="M33 42a7 7 0 0 1 10 0M35.5 44.5a3.5 3.5 0 0 1 5 0" fill="none" stroke="var(--blue)" stroke-width="1.6"/></svg>
      WLAN<br>Ausleuchtung
    </div>
    <div class="feature" style="left:361px;top:356px">
      <svg viewBox="0 0 52 52"><rect x="1" y="1" width="50" height="50" rx="9" fill="#fff" stroke="var(--blue)" stroke-width="1.2"/>
        <rect x="12" y="10" width="17" height="31" fill="var(--orange)"/><rect x="29" y="20" width="10" height="21" fill="var(--orange)"/>
        <g fill="#fff"><rect x="15" y="14" width="4" height="4"/><rect x="22" y="14" width="4" height="4"/><rect x="15" y="22" width="4" height="4"/><rect x="22" y="22" width="4" height="4"/><rect x="15" y="30" width="4" height="4"/><rect x="22" y="30" width="4" height="4"/><rect x="32" y="25" width="4" height="4"/></g>
        <path d="M34 39a7 7 0 0 1 10 0M36.5 41.5a3.5 3.5 0 0 1 5 0" fill="none" stroke="var(--blue)" stroke-width="1.6"/></svg>
      WLAN<br>Infrastruktur
    </div>

    <div class="photo-main" role="img" aria-label="Foto: Hände auf Bauplänen und Planrollen"
      style="width:360px;height:300px;background:linear-gradient(135deg,#e8e6e2,#cfc9c1 50%,#f2efeb);clip-path:polygon(0 40%,100% 0,100% 100%,0 100%)"></div>
    <div class="photo-round" role="img" aria-label="Foto: Hände tippen auf einer Laptop-Tastatur"
      style="left:194px;top:451px;background:linear-gradient(160deg,#f1f1f1,#b8bcc2 55%,#6d7278)"></div>

    <div class="advantages" style="left:15px;top:562px;width:223px;height:195px;padding-top:15px">
      <h3>Ihre Vorteile auf einen Blick:</h3>
      <ul>
        <li>Planung und Ausleuchtung vom Profi</li>
        <li>Konfiguration und Montage durch<br>zertifizierte Techniker</li>
        <li>Kompetente und objektive Beratung<br>vom Fachmann</li>
        <li>Maximale Effizienz und<br>kalkulierbare Kosten</li>
      </ul>
    </div>

    <svg class="wave-bottom" viewBox="0 0 546 80" preserveAspectRatio="none">
      <path d="M240 80V42C350 20 450 8 546 6V80Z" fill="var(--blue-light)"/>
      <path d="M240 80V56C350 38 450 30 546 30V80Z" fill="var(--blue-mid)"/>
      <path d="M0 80V66C180 54 380 48 546 50V80Z" fill="var(--blue-deep)"/>
    </svg>
    <div class="contact">info@quarvelo-netz.de | www.quarvelo-netz.de</div>
  </section>
</div>
</body>
</html>
```